Manuka honey wholesales and exports

We need business cards for our honey distribution company based in New Zealand. We supply shops locally and export Manuka honey around the world.
We deal with a very high quality and 100% natural product that can be used for medical, general health as well as food. We are looking business cards that show our honey products are of a high quality with a modern look.

Target Market(s)

Health and medical retailers and importers

Industry/Entity Type

Wholesale

Contact Information for Business Card

Tevin Apiary NZ Limited

www.tevinapiarynz.example

Derek Fawley

M +64 219036482

E tevinapiarynz@mailbox.example

PO Box 58-214
Takapuna
North Shore
Auckland
New Zealand

Font styles to use
Serif

Requirements
Must have
• (Tevin Apiary NZ Limited) with some artwork on one side and all details on the other side.
Nice to have
• I have seen a very simple card with large yellow and black stripes on one side with a company name.. looked clean and simple so something similar or just let the creative beast inside you take over and we will see what you can come up with.

```html
<!DOCTYPE html>
<html lang="en">
<head>
<meta charset="utf-8">
<title>Tevin Apiary NZ Limited – Business Cards</title>
<link href="https://fonts.googleapis.com/css2?family=Open+Sans:wght@400;600;700&display=swap" rel="stylesheet">
<style>
  :root {
    --page-bg: #e9e6e0;
    --card-white: #f7f7f5;
    --ink: #2b2b2b;
    --ink-soft: #3c3c3c;
    --honey-orange: #e08a1e;
    --honey-deep: #d9851c;
    --stripe-orange: #e9a24f;
    --stripe-yellow: #f0bf45;
  }
  * { box-sizing: border-box; margin: 0; padding: 0; }
  html, body {
    width: 1200px; height: 800px; overflow: hidden;
    background: var(--page-bg);
    font-family: "Open Sans", Arial, sans-serif;
  }
  .canvas {
    width: 1200px; height: 800px;
    display: flex; align-items: center; justify-content: center; gap: 40px;
  }
  .card {
    position: relative;
    width: 540px; height: 309px;
    background: var(--card-white);
    box-shadow: 0 10px 28px rgba(0,0,0,.18);
    overflow: hidden;
  }
  /* brand lockup */
  .brand {
    position: absolute;
    display: flex; align-items: center; gap: 12px;
  }
  .brand-dot {
    border-radius: 50%;
    background: var(--honey-orange);
    flex: none;
  }
  .brand-name {
    color: var(--honey-deep);
    font-weight: 600;
    line-height: 1.15;
  }
  /* details side */
  .card--details .brand { left: 34px; bottom: 44px; }
  .card--details .brand-dot { width: 44px; height: 44px; }
  .card--details .brand-name { font-size: 19px; width: 150px; }
  .contact {
    position: absolute; left: 240px; top: 58px;
    color: var(--ink-soft); font-size: 12.5px; line-height: 1.45;
  }
  .contact-name {
    font-weight: 700; font-size: 19px; color: var(--ink);
    margin-bottom: 8px;
  }
  .contact-row { display: flex; align-items: flex-start; gap: 10px; margin-bottom: 3px; }
  .contact-row svg { width: 12px; height: 12px; margin-top: 3px; flex: none; }
  .contact-row--web { margin-top: 8px; }
  /* brand side */
  .card--brand .brand { left: 96px; top: 108px; gap: 16px; }
  .card--brand .brand-dot { width: 64px; height: 64px; }
  .card--brand .brand-name { font-size: 27px; width: 230px; }
  .stripe-thin {
    position: absolute; left: 0; right: 0; bottom: 30px; height: 7px;
    background: var(--stripe-orange);
  }
  .stripe-wide {
    position: absolute; left: 0; right: 0; bottom: 0; height: 24px;
    background: var(--stripe-yellow);
  }
</style>
</head>
<body>
<main class="canvas">
  <section class="card card--details">
    <div class="contact">
      <p class="contact-name">Derek Fawley</p>
      <p class="contact-row">
        <svg viewBox="0 0 12 12"><rect x="3" y="0.5" width="6" height="11" rx="1.2" fill="none" stroke="var(--honey-orange)" stroke-width="1.2"/></svg>
        <span>+64 219036482</span>
      </p>
      <p class="contact-row">
        <svg viewBox="0 0 12 12"><rect x="0.5" y="2" width="11" height="8" fill="var(--honey-orange)"/><path d="M0.5 2 L6 6.5 L11.5 2" fill="none" stroke="#fff" stroke-width="1"/></svg>
        <span>tevinapiarynz@mailbox.example</span>
      </p>
      <p class="contact-row">
        <svg viewBox="0 0 12 12"><path d="M6 11.5 C3 7.5 2 6 2 4.2 A4 4 0 0 1 10 4.2 C10 6 9 7.5 6 11.5Z" fill="var(--honey-orange)"/><circle cx="6" cy="4.3" r="1.5" fill="#fff"/></svg>
        <span>PO Box 58-214, Takapuna<br>North Shore, Auckland, New Zealand</span>
      </p>
      <p class="contact-row contact-row--web">
        <svg viewBox="0 0 12 12"><circle cx="6" cy="6" r="5" fill="none" stroke="var(--honey-orange)" stroke-width="1.1"/><ellipse cx="6" cy="6" rx="2.2" ry="5" fill="none" stroke="var(--honey-orange)" stroke-width="0.9"/><path d="M1 6 H11" stroke="var(--honey-orange)" stroke-width="0.9"/></svg>
        <span>www.tevinapiarynz.example</span>
      </p>
    </div>
    <div class="brand">
      <span class="brand-dot"></span>
      <span class="brand-name">Tevin Apiary NZ Limited</span>
    </div>
  </section>

  <section class="card card--brand">
    <div class="brand">
      <span class="brand-dot"></span>
      <span class="brand-name">Tevin Apiary NZ Limited</span>
    </div>
    <div class="stripe-thin"></div>
    <div class="stripe-wide"></div>
  </section>
</main>
</body>
</html>
```